New Design for Water Vending Machine

Re-design graphics for face plate of water jug vending machine.

Attached are the following:
-Picture of the current face plate for the vending machine. The layout and workflow of the system have been changed.
-Picture of the new face plate without a decal installed.
-Picture of an actual installation of these vending machines for reference.
-DXF File with layout of the face plate
-PDF File with layout notes

The graphics will be printed on a lexan decal. There will be holes cutout for the following:
-Corvel Credit card reader
-Coin reject button
-Coin slot
-4 x Buttons
-Change return
Each of the cutouts should be approximately 5mm larger in all directions than the cutout size on the DXF file.

The flow of the system is as follows:
1. Insert Coins or tap Paymora/Credit/PrePaid Card
2. Press 'Format' button until desired bottle size is displayed.
3. Press 'Start' to begin filling.
'Pause' Button may be pressed during fill to switch containers or temporarily pause fill.
A poster has also been attached that is currently displayed above the prototype machines for customer reference.

Note that the bottom button is not currently used. Perhaps the design could include a window of sorts to add a label to it down the road.

The logos for TallyPay, Quova and Paymora Swift could be displayed near the cutout for the Corvel system.

The phrase 'Premium Drinking Water processed by Reverse Osmosis' should be displayed somewhere on the plate.

Dimensions of the face plate are 12.75" wide x 29.75" high. Dimensions of the graphics will be 10.25" x 27".

The display window will simply be clear lexan. No material will be cutout. Buffer space around display window should be 7mm.

Requirements
Must have
• Vibrant colors, and be eye catching. We want customers to be visually appealed by the machine. It should also follow a blue color theme. Text needs to be clearly layed out, and be concise.

```html
<!DOCTYPE html>
<html lang="en">
<head>
<meta charset="utf-8">
<title>Water Vending Machine Face Plate</title>
<link rel="stylesheet" href="https://fonts.googleapis.com/css2?family=Arimo:ital,wght@0,400;0,700;1,700&display=swap">
<style>
  :root {
    --page: #ffffff;
    --plate: #cfcfcf;
    --plate-edge: #1a1a1a;
    --water-top: #dcf5f9;
    --water-mid: #8dd0e3;
    --water-bottom: #4faad0;
    --step-box: #1a7596;
    --text-light: #ffffff;
    --cutout: #ffffff;
    --cutout-edge: #111111;
    --badge: #17365d;
  }
  html, body {
    margin: 0;
    padding: 0;
    width: 888px;
    height: 1200px;
    overflow: hidden;
    background: var(--page);
  }
  .face-plate-art {
    display: block;
    width: 888px;
    height: 1200px;
    font-family: "Arimo", Arial, sans-serif;
  }
  .plate { fill: var(--plate); stroke: var(--plate-edge); stroke-width: 1.5; filter: drop-shadow(0 4px 10px rgba(0,0,0,0.35)); }
  .mount-hole { fill: none; stroke: var(--cutout-edge); stroke-width: 1.6; }
  .step-box { fill: var(--step-box); opacity: 0.95; }
  .cutout { fill: var(--cutout); stroke: var(--cutout-edge); stroke-width: 1.4; }
  .display-frame { fill: var(--step-box); }
  .screw { fill: #ffffff; stroke: var(--cutout-edge); stroke-width: 1.3; }
  .button-hole { fill: var(--cutout); stroke: var(--cutout-edge); stroke-width: 1.6; }
  .step-number { fill: var(--text-light); font-weight: 700; font-size: 46px; }
  .step-text { fill: var(--text-light); font-weight: 700; font-size: 10.4px; }
  .card-badge { fill: var(--badge); }
  .card-name { fill: var(--text-light); font-weight: 700; font-size: 8px; }
  .headline { fill: var(--text-light); font-weight: 700; font-style: italic; font-size: 29px; }
  .subline { fill: var(--text-light); font-weight: 700; font-style: italic; font-size: 18.5px; }
</style>
</head>
<body>
<svg class="face-plate-art" viewBox="0 0 888 1200" xmlns="http://www.w3.org/2000/svg">
  <defs>
    <linearGradient id="water-fill" x1="0" y1="0" x2="0" y2="1">
      <stop offset="0" stop-color="var(--water-top)"/>
      <stop offset="0.35" stop-color="var(--water-mid)"/>
      <stop offset="0.75" stop-color="var(--water-bottom)"/>
      <stop offset="1" stop-color="var(--water-bottom)"/>
    </linearGradient>
  </defs>

  <!-- metal face plate -->
  <rect class="plate" x="202" y="35" width="484" height="1129"/>

  <g class="mounting-holes">
    <rect class="mount-hole" x="222.5" y="58" width="10" height="10"/>
    <rect class="mount-hole" x="330" y="58" width="10" height="10"/>
    <rect class="mount-hole" x="437.6" y="58" width="10" height="10"/>
    <rect class="mount-hole" x="545" y="58" width="10" height="10"/>
    <rect class="mount-hole" x="652.7" y="58" width="10" height="10"/>
    <rect class="mount-hole" x="222.5" y="177" width="10" height="10"/>
    <rect class="mount-hole" x="652.7" y="177" width="10" height="10"/>
    <rect class="mount-hole" x="222.5" y="297" width="10" height="10"/>
    <rect class="mount-hole" x="652.7" y="297" width="10" height="10"/>
    <rect class="mount-hole" x="222.5" y="416" width="10" height="10"/>
    <rect class="mount-hole" x="652.7" y="416" width="10" height="10"/>
    <rect class="mount-hole" x="222.5" y="535" width="10" height="10"/>
    <rect class="mount-hole" x="652.7" y="535" width="10" height="10"/>
    <rect class="mount-hole" x="222.5" y="655" width="10" height="10"/>
    <rect class="mount-hole" x="652.7" y="655" width="10" height="10"/>
    <rect class="mount-hole" x="222.5" y="774" width="10" height="10"/>
    <rect class="mount-hole" x="652.7" y="774" width="10" height="10"/>
    <rect class="mount-hole" x="222.5" y="894" width="10" height="10"/>
    <rect class="mount-hole" x="652.7" y="894" width="10" height="10"/>
    <rect class="mount-hole" x="222.5" y="1013" width="10" height="10"/>
    <rect class="mount-hole" x="652.7" y="1013" width="10" height="10"/>
    <rect class="mount-hole" x="222.5" y="1132" width="10" height="10"/>
    <rect class="mount-hole" x="330" y="1132" width="10" height="10"/>
    <rect class="mount-hole" x="437.6" y="1132" width="10" height="10"/>
    <rect class="mount-hole" x="545" y="1132" width="10" height="10"/>
    <rect class="mount-hole" x="652.7" y="1132" width="10" height="10"/>
  </g>

  <!-- decal background -->
  <rect class="decal" x="247" y="88" width="389" height="1024" rx="11" fill="url(#water-fill)" role="img" aria-label="Water droplets and bubbles pattern in light cyan to blue"/>

  <!-- display window -->
  <rect class="display-frame" x="325" y="97" width="234" height="47" rx="5"/>
  <rect class="cutout display-window" x="332" y="103" width="222" height="35"/>
  <circle class="screw" cx="312.5" cy="96" r="2.5"/>
  <circle class="screw" cx="569.5" cy="96" r="2.5"/>
  <circle class="screw" cx="312.5" cy="143.5" r="2.5"/>
  <circle class="screw" cx="569.5" cy="143.5" r="2.5"/>

  <!-- accepted cards -->
  <rect class="card-badge" x="522" y="167" width="34" height="21" rx="2"/>
  <text class="card-name" x="539" y="180.5" text-anchor="middle">Quova</text>
  <rect class="card-badge" x="565" y="167" width="34" height="21" rx="2"/>
  <text class="card-name" x="582" y="180.5" text-anchor="middle">TallyPay</text>

  <!-- card reader cutout -->
  <rect class="cutout card-reader" x="496.5" y="200.5" width="127.5" height="158"/>
  <circle class="screw" cx="497" cy="192.5" r="3"/>
  <circle class="screw" cx="624" cy="192.5" r="3"/>
  <circle class="screw" cx="522" cy="369" r="3"/>
  <circle class="screw" cx="598.5" cy="369" r="3"/>

  <!-- coin reject and coin slot -->
  <circle class="button-hole" cx="320" cy="225" r="5"/>
  <circle class="button-hole" cx="353" cy="225" r="7.5"/>
  <rect class="cutout coin-slot" x="376.5" y="203" width="3" height="45" rx="1.5"/>
  <circle class="button-hole" cx="397.5" cy="225" r="5"/>

  <!-- step 1 -->
  <rect class="step-box" x="270.5" y="268" width="209.5" height="57" rx="6"/>
  <text class="step-number" x="302" y="313" text-anchor="middle">1</text>
  <text class="step-text" x="322" y="289">Insert Coins or tap</text>
  <text class="step-text" x="322" y="301">Paymora/Credit/PrePaid</text>
  <text class="step-text" x="322" y="313">Card</text>

  <!-- step 2 -->
  <rect class="step-box" x="353" y="465" width="242" height="58" rx="6"/>
  <text class="step-number" x="391.5" y="511" text-anchor="middle">2</text>
  <text class="step-text" x="417" y="487">Press 'Format' button</text>
  <text class="step-text" x="417" y="499">until desired bottle size</text>
  <text class="step-text" x="417" y="511">is displayed</text>
  <circle class="button-hole" cx="560.5" cy="494" r="19"/>

  <!-- step 3 -->
  <rect class="step-box" x="353" y="579" width="242" height="58" rx="6"/>
  <text class="step-number" x="391.5" y="625" text-anchor="middle">3</text>
  <text class="step-text" x="417" y="605">Press 'Start'</text>
  <text class="step-text" x="417" y="617">to begin filling</text>
  <circle class="button-hole" cx="560.5" cy="607.5" r="19"/>

  <!-- pause -->
  <rect class="step-box" x="353" y="693" width="242" height="58" rx="6"/>
  <text class="step-text" x="379" y="714">'Pause' Button may be pressed</text>
  <text class="step-text" x="379" y="726">during fill to switch containers</text>
  <text class="step-text" x="379" y="738">or temporarily pause fill</text>
  <circle class="button-hole" cx="560.5" cy="722" r="19"/>

  <!-- spare button label window -->
  <rect class="step-box" x="353" y="805.5" width="242" height="58" rx="6"/>
  <circle class="button-hole" cx="560.5" cy="835" r="19"/>

  <!-- button mounting screws -->
  <circle class="screw" cx="317.5" cy="542" r="5"/>
  <circle class="screw" cx="317.5" cy="675" r="5"/>
  <circle class="screw" cx="317.5" cy="808" r="5"/>

  <!-- headline -->
  <text class="headline" x="442.5" y="922" text-anchor="middle">Premium Drinking Water</text>
  <text class="subline" x="441" y="952" text-anchor="middle">processed by Reverse Osmosis</text>

  <!-- change return -->
  <rect class="cutout change-return" x="278" y="991" width="122" height="57"/>
  <circle class="screw" cx="265" cy="1019" r="3"/>
  <circle class="screw" cx="413" cy="1019" r="3"/>
</svg>
</body>
</html>
```